Business Cards Needed For Veterinary Business

Looking for a business card design for a veterinary blood bank. We would like it to be clean and professional on appearance but still warm and inviting. We would like to utilize our logo and similar coloring. We will use our phone number, email, website, employee name, employee title.

We do not want a bunch of animated animal photos but do not need the style to be as clinical as a laboratory or human medical procedure office.

We are looking for some creative ideas to choose from so that we can generate a standout professional business card for our management team to utilize.

Target Market(s)

professionals

Industry/Entity Type

veterinary

Contact Information for Business Card

employee name, employee title, phone number, website URL, email

Font styles to use
Sans Serif

Colors
0054AA
0677BA
7BADD7
CADEEF
E8F1F8
EB3D1F
EC4F4E
F09395
F8D3D4
FCEDEE

Requirements
Nice to have
• creative design
Should not have
• animated photos

```html
<!DOCTYPE html>
<html lang="en">
<head>
<meta charset="utf-8">
<title>Larkspur Animal Transfusion Center – Business Cards</title>
<link href="https://fonts.googleapis.com/css2?family=Montserrat:wght@500;600;700;800&display=swap" rel="stylesheet">
<style>
  :root {
    --blue: #0054AA;
    --red: #EB3D1F;
    --pink-mid: #F09395;
    --pink-light: #F8D3D4;
    --card-bg: #FCEDEE;
    --stage: #F4E4E5;
    --ink: #2b2b33;
  }
  * { margin: 0; padding: 0; box-sizing: border-box; }
  html, body { width: 1200px; height: 900px; overflow: hidden; }
  body {
    background: var(--stage);
    font-family: "Montserrat", Arial, sans-serif;
    position: relative;
  }
  .card {
    position: absolute;
    background: var(--card-bg);
    overflow: hidden;
    box-shadow: 0 10px 30px rgba(160, 70, 80, 0.18);
  }
  .card-stripe {
    position: absolute; left: 0; right: 0; bottom: 0; height: 7px;
    display: flex;
  }
  .card-stripe .stripe-blue { flex: 1; background: var(--blue); }
  .card-stripe .stripe-red { flex: 1; background: var(--red); }

  /* Front */
  .card-front { left: 70px; top: 290px; width: 560px; height: 320px; }
  .art-cat-front {
    position: absolute; left: 0; top: 70px; width: 150px; height: 243px;
    background: linear-gradient(120deg, rgba(240,147,149,0.28), rgba(248,211,212,0.15));
    border-top-right-radius: 70px;
  }
  .art-dog-front {
    position: absolute; right: 0; top: 0; width: 120px; height: 230px;
    background: linear-gradient(200deg, rgba(240,147,149,0.28), rgba(248,211,212,0.12));
    border-bottom-left-radius: 60px;
  }
  .brand {
    position: absolute; left: 148px; top: 120px;
    display: flex; align-items: center; gap: 14px;
  }
  .brand-dot {
    width: 62px; height: 62px; border-radius: 50%;
    background: var(--red); flex: none;
  }
  .brand-text { color: var(--red); font-weight: 700; line-height: 1.05; }
  .brand-short { font-size: 38px; letter-spacing: 0.5px; display: block; }
  .brand-long { font-size: 12px; letter-spacing: 0.4px; display: block; margin-top: 5px; }

  /* Back */
  .card-back { left: 800px; top: 170px; width: 320px; height: 560px; }
  .art-dog-back {
    position: absolute; left: 0; top: 60px; width: 120px; height: 250px;
    background: linear-gradient(180deg, rgba(240,147,149,0.28), rgba(248,211,212,0.1));
    border-top-right-radius: 60px;
  }
  .art-cat-back {
    position: absolute; right: 0; top: 60px; width: 130px; height: 200px;
    background: linear-gradient(180deg, rgba(240,147,149,0.28), rgba(248,211,212,0.1));
    border-top-left-radius: 60px;
  }
  .cross { position: absolute; left: 150px; top: 40px; width: 38px; height: 38px; }
  .back-panel { position: absolute; left: 0; top: 0; width: 320px; height: 560px; }
  .person { position: absolute; left: 38px; top: 352px; right: 20px; }
  .person-first, .person-last {
    color: var(--red); font-weight: 800; text-transform: uppercase; display: block; line-height: 1;
  }
  .person-first { font-size: 22px; }
  .person-last { font-size: 32px; margin-top: 2px; }
  .person-title {
    color: var(--blue); font-weight: 700; font-size: 14px; margin-top: 8px; display: block;
  }
  .contact { margin-top: 22px; list-style: none; color: var(--ink); font-size: 13px; font-weight: 500; }
  .contact li { display: flex; gap: 12px; margin-bottom: 4px; }
  .contact .label { width: 22px; flex: none; }
</style>
</head>
<body>

<section class="card card-front" aria-label="Business card front">
  <div class="art-cat-front" role="img" aria-label="Faint line illustration of a cat"></div>
  <div class="art-dog-front" role="img" aria-label="Faint line illustration of a dog"></div>
  <div class="brand">
    <span class="brand-dot"></span>
    <span class="brand-text">
      <span class="brand-short">LARKSPUR</span>
      <span class="brand-long">ANIMAL TRANSFUSION CENTER</span>
    </span>
  </div>
  <div class="card-stripe"><span class="stripe-blue"></span><span class="stripe-red"></span></div>
</section>

<section class="card card-back" aria-label="Business card back">
  <div class="art-dog-back" role="img" aria-label="Faint line illustration of a dog"></div>
  <div class="art-cat-back" role="img" aria-label="Faint line illustration of a cat"></div>
  <svg class="cross" viewBox="0 0 38 38" aria-hidden="true">
    <rect x="13" y="0" width="12" height="38" fill="var(--red)"/>
    <rect x="0" y="13" width="38" height="12" fill="var(--red)"/>
  </svg>
  <svg class="back-panel" viewBox="0 0 320 560" aria-hidden="true">
    <path d="M0 330 L250 282 Q300 272 320 315 L320 560 L0 560 Z" fill="var(--pink-light)" opacity="0.45"/>
    <path d="M0 330 L250 282 Q300 272 320 315" fill="none" stroke="var(--red)" stroke-width="6"/>
    <path d="M0 318 L250 270 Q302 260 320 300" fill="none" stroke="var(--red)" stroke-width="1.5"/>
  </svg>
  <div class="person">
    <span class="person-first">Daniel</span>
    <span class="person-last">Moreno</span>
    <span class="person-title">OWNER</span>
    <ul class="contact">
      <li><span class="label">M :</span><span>(555) 014-2283</span></li>
      <li><span class="label">E :</span><span>daniel@larkspurpets.com</span></li>
      <li><span class="label">W :</span><span>larkspurpets.com</span></li>
    </ul>
  </div>
  <div class="card-stripe"><span class="stripe-blue"></span><span class="stripe-red"></span></div>
</section>

</body>
</html>
```